Business Identity Stationary

Already have the logo which is in the attached files so only need the Business STationary
1) Double Sided Business Card
2) Letterhead
3) Presentation folder with business card holder on inside cover
4) WIth compliments slip
See information for business cards, letterhead and presentation folder below.
http://files.pixelbazaar-example.com/img/771204/40612/40612_3918825_771204_thumb.jpg
Updates

This should be a simply job using a logo we already had designed along with a little device. I suggest using the device off center and perhaps lower in the corner in an abstract way. Also the logo device could be used as a watermark for the letterhead. The designer who created the logo presented something that I think works well for a business card. The front of the double sided business card could have the name logo small for the website address and only use the Lime device on the front. Then on the back could be the name Brevar Consulting logo.

Please note that for the business card the black and lime green background do look good. Also please think of using the lime device separately in an unusual way.

It has been brought to my attention that.my budget was far to low. Hopefully this.will attract you to the project. 

The parent company of Brevar Consulting is TallHeron investments. I have uploaded a file of the Tall Heron business card I really like. Perhaps use this business card as a guide to the type of modern and clean style I am looking for. It also works to have the Brevar Consultign and Tall Heron similar.

Reason: Still haven't received anything exactly right.

Industry/Entity Type

Business

Font styles to use
Sans Serif

Colors
9bcb3c
000000
5c5c5c
add136
cadf82
eaf2cf
f9fbf2
1b1b1b
757575

Requirements
Must have
• 1) Double Sided Business Card
Marta Delvorin
Director
Tel: +505 8290 3357
Email: mkd@brevarconsulting-example.com
Website: www.brevarconsulting-example.com

Everett Delvorin
Director
Tel: +505 8290 3362
Email: ekd@brevarconsulting-example.com

Lucia Pardo Ventrosa
Director
Tel: 8442 6183
Email: lpv@brevarconsulting-example.com

2) Letterhead
Logo
Lime Logo Device
Website Address: www.brevarconsulting-example.com
Small print on bottom: Brevar Consulting a Tall Heron Investment Company SA. RUC K0720000483915

3) Presentation Folder
Traditional Presentation folder with inside front cover spot for the insertion of business card.

4) With Compliments slip

```html
<!DOCTYPE html>
<html lang="en">
<head>
<meta charset="utf-8">
<title>Brevar Consulting – Business Card</title>
<link rel="stylesheet" href="https://fonts.googleapis.com/css2?family=Open+Sans:wght@400;600&display=swap">
<style>
  :root {
    --lime: #9bcb3c;
    --lime-light: #add136;
    --ink: #1b1b1b;
    --grey: #5c5c5c;
    --paper: #f9fbf2;
    --white: #ffffff;
    --card-dark: #262626;
    --backdrop: #2b2b2b;
  }
  * { margin: 0; padding: 0; box-sizing: border-box; }
  html, body {
    width: 1200px;
    height: 900px;
    overflow: hidden;
    background: var(--backdrop);
    font-family: "Open Sans", sans-serif;
  }
  .card {
    position: absolute;
    left: 354px;
    width: 488px;
    height: 271px;
    box-shadow: 0 3px 8px rgba(0, 0, 0, 0.45);
  }
  .card--front { top: 157px; background: var(--white); }
  .card--back { top: 466px; background: var(--card-dark); }

  .wordmark {
    position: absolute;
    font-weight: 400;
    letter-spacing: 0.02em;
    white-space: nowrap;
  }
  .card--front .wordmark {
    top: 40px;
    left: 0;
    width: 100%;
    text-align: center;
    font-size: 36px;
    color: var(--ink);
  }
  .card--back .wordmark {
    right: 22px;
    top: 170px;
    font-size: 32px;
    color: var(--white);
  }

  .name-band {
    position: absolute;
    top: 141px;
    left: 0;
    width: 100%;
    height: 27px;
    background: linear-gradient(90deg, var(--lime), var(--lime-light));
    color: var(--white);
    font-size: 17px;
    letter-spacing: 0.04em;
    text-align: center;
    line-height: 27px;
  }
  .role {
    position: absolute;
    top: 172px;
    width: 100%;
    text-align: center;
    font-size: 13px;
    color: var(--ink);
  }
  .contact {
    position: absolute;
    left: 30px;
    top: 206px;
    list-style: none;
    font-size: 11.5px;
    color: var(--grey);
  }
  .contact li {
    display: flex;
    align-items: center;
    gap: 12px;
    height: 17px;
  }
  .contact svg { width: 11px; height: 11px; flex: none; }
  .website {
    position: absolute;
    right: 30px;
    top: 223px;
    font-size: 11.5px;
    color: var(--ink);
  }
  .website .accent { color: var(--lime); }
</style>
</head>
<body>

<section class="card card--front" aria-label="Business card front">
  <div class="wordmark">Brevar Consulting</div>
  <div class="name-band">MARTA DELVORIN</div>
  <div class="role">Director</div>
  <ul class="contact">
    <li>
      <svg viewBox="0 0 11 11" aria-hidden="true"><rect x="2.5" y="0.5" width="6" height="10" rx="1" fill="none" stroke="#9bcb3c" stroke-width="1.2"/><rect x="4" y="2" width="3" height="4" fill="#9bcb3c"/></svg>
      +505 8290 3357
    </li>
    <li>
      <svg viewBox="0 0 11 11" aria-hidden="true"><rect x="0.5" y="2" width="10" height="7" fill="#9bcb3c"/><path d="M0.5 2 L5.5 6 L10.5 2" fill="none" stroke="#ffffff" stroke-width="1"/></svg>
      mkd@brevarconsulting-example.com
    </li>
  </ul>
  <div class="website">www.<span class="accent">brevarconsulting-example</span>.com</div>
</section>

<section class="card card--back" aria-label="Business card back">
  <div class="wordmark">Brevar Consulting</div>
</section>

</body>
</html>
```